Mock up Blog Design for midwife that works in a hospital setting

We are looking to have a design created for a midwife. This blog will be used to share information or experiences related to pregnancy, child birth and motherhood with its readership. It should convey a feeling of warmth and security to women who are looking for a partner in the birthing processes.

We are asking you to design the layout, not code it up. This is a concept project only.

NOtes from the midwife

​So I'm just going to put in links to a few blogs and say what I like and don't like about each one:

pelwinhartcote.com.au/blog/

I like how there is a colorful background that has to do with her books; maybe mine could have a background with baby stuff in the background. It's also nice how there's an index of recent postings with the subject listed and how the postings are sorted by date, all on the same page.

www.brightbottlejournal.com

I like that this one is set up like a website with tabs for resources, a bio, reader comments, etc.

freshparentnotes.tallowgrove.org

This blog has a very calming color scheme, which is welcoming. I like that there's a picture for every posting, and that at the bottom of the posting there is a little glossary with the subjects that are covered in the posting. Also, I like the way that the date of each blog is done.

laboursidechats.blogspot.com

This one is really funny, and similar in intention to the one that I want to do. I like that she has a glossary of medical terms so that readers can look them up.

General comments:
I'm not sure how much TBWH wants their logo on my blog or in the blog name...
I would like to be able to vet comments before they appear on the blog, so that if there's an inappropriate one, I can screen it out.
I would also like to be able to see how many people have viewed the site.
Updates

Target Market(s)

Pregnant mothers, new moms, hopeful moms

Industry/Entity Type

Hospital

Requirements
Must have
• Incorporation of the logo and at least one of the photographs that will be provided In the header
Should not have
• Should not look canned, rigid or boxy.

```html
<!DOCTYPE html>
<html lang="en">
<head>
<meta charset="utf-8">
<title>Dawnlight Midwifery – Blog</title>
<link rel="stylesheet" href="https://fonts.googleapis.com/css2?family=Open+Sans:wght@400;600&family=Ubuntu:wght@300;400&display=swap">
<style>
  :root {
    --pink: #f76a8c;
    --mint: #c5e8dc;
    --mint-edge: #a9d8c8;
    --date-mint: #a3e3d7;
    --page-bg: #efefef;
    --white: #ffffff;
    --ink: #333333;
    --body-text: #666666;
    --side-text: #444444;
    --muted: #777777;
    --meta-bg: #f2f2f2;
  }
  * { box-sizing: border-box; margin: 0; padding: 0; }
  html, body { width: 1200px; height: 912px; overflow: hidden; }
  body {
    position: relative;
    background: var(--page-bg);
    font-family: "Open Sans", Arial, sans-serif;
    color: var(--ink);
  }
  .top-strip { position: absolute; left: 0; top: 0; width: 1200px; height: 71px; background: var(--white); }
  .nav-band { position: absolute; left: 0; top: 71px; width: 1200px; height: 47px; background: var(--pink); }
  .brand {
    position: absolute; left: 68px; top: 0; width: 196px; height: 138px;
    background: var(--white);
    display: flex; flex-direction: column; align-items: center; justify-content: center; gap: 8px;
  }
  .brand-dot { width: 34px; height: 34px; border-radius: 50%; background: var(--pink); }
  .brand-name { font-family: "Ubuntu", sans-serif; font-size: 17px; font-weight: 400; color: var(--pink); text-align: center; line-height: 1.1; }
  .main-nav { position: absolute; left: 292px; top: 71px; height: 47px; display: flex; align-items: center; gap: 31px; list-style: none; }
  .main-nav li { font-family: "Ubuntu", sans-serif; font-size: 15px; color: var(--white); text-transform: uppercase; white-space: nowrap; }

  .post-panel { position: absolute; left: 68px; top: 151px; width: 749px; height: 761px; background: var(--white); }
  .post-date {
    position: absolute; left: 10px; top: 188px; width: 58px; height: 60px;
    background: var(--date-mint); color: var(--white);
    font-size: 15px; text-align: center; line-height: 23px; padding-top: 7px;
  }
  .post-title {
    position: absolute; left: 108px; top: 179px; width: 670px; text-align: center;
    font-family: "Ubuntu", sans-serif; font-weight: 300; font-size: 19.5px; color: var(--ink);
    text-transform: uppercase; white-space: nowrap;
  }
  .post-photo {
    position: absolute; left: 108px; top: 225px; width: 670px; height: 447px;
    background: radial-gradient(ellipse at 48% 55%, #f6a3b5 0%, #f1d8d6 35%, #ece6df 70%, #e6ddd3 100%);
  }
  .post-excerpt {
    position: absolute; left: 110px; top: 686px; width: 668px;
    font-size: 15px; line-height: 29px; color: var(--body-text);
    letter-spacing: -0.15px; white-space: nowrap;
  }
  .post-excerpt .read-more { color: #111; }
  .post-meta {
    position: absolute; left: 108px; top: 807px; width: 669px; height: 31px;
    background: var(--meta-bg); font-size: 12px; color: var(--muted);
    display: flex; align-items: center; padding: 0 16px;
  }
  .post-meta .category { color: var(--pink); text-transform: uppercase; margin-left: 4px; }
  .post-meta .stats { margin-left: auto; display: flex; gap: 14px; align-items: center; }
  .post-meta .stat { display: flex; align-items: center; gap: 5px; }

  .sidebar {
    position: absolute; left: 817px; top: 151px; width: 344px; height: 761px;
    background: var(--mint); border-left: 2px solid var(--mint-edge);
  }
  .widget-heading {
    position: absolute; height: 33px; background: var(--pink); color: var(--white);
    font-family: "Ubuntu", sans-serif; font-size: 15px; font-weight: 400; text-transform: uppercase;
    display: flex; align-items: center; justify-content: center;
  }
  .welcome-heading { left: 837px; top: 190px; width: 307px; }
  .categories-heading { left: 836px; top: 652px; width: 307px; }
  .author-photo {
    position: absolute; left: 895px; top: 236px; width: 190px; height: 190px; border-radius: 50%;
    border: 6px solid var(--white);
    background: radial-gradient(circle at 50% 45%, #c9a9a6 0%, #b57c84 40%, #f2eeee 75%);
  }
  .author-intro {
    position: absolute; left: 841px; top: 437px; width: 310px;
    font-size: 15.5px; line-height: 29px; color: var(--side-text);
    letter-spacing: -0.2px; white-space: nowrap;
  }
  .social-links { position: absolute; left: 872px; top: 572px; display: flex; gap: 11px; list-style: none; }
  .social-links li { width: 30px; height: 30px; border-radius: 50%; background: var(--white); }
  .category-select {
    position: absolute; left: 836px; top: 695px; width: 307px; height: 50px; background: var(--white);
    display: flex; align-items: center; padding: 0 16px 0 22px; font-size: 15px; color: #9a9a9a;
  }
  .category-select svg { margin-left: auto; }
</style>
</head>
<body>
  <div class="top-strip"></div>
  <div class="nav-band"></div>
  <a class="brand">
    <span class="brand-dot"></span>
    <span class="brand-name">Dawnlight Midwifery</span>
  </a>
  <ul class="main-nav">
    <li>Home</li><li>About Me</li><li>Categories</li><li>Resources</li><li>Glossary</li><li>Gallery</li><li>Ask the Midwife</li>
  </ul>

  <div class="post-panel"></div>
  <div class="post-date">MAY<br>17</div>
  <h1 class="post-title">Everything you need to know about assisted deliveries</h1>
  <div class="post-photo" role="img" aria-label="Newborn baby asleep on a cream knitted blanket, wearing a pink knitted hat with a flower and ruffled pink bloomers"></div>
  <p class="post-excerpt">An assisted delivery means when a doctor uses an instrument such as forceps or ventouse cup<br>(sometimes called a Vela cup) to deliver your baby’s head. Around one in eight women have to<br>deliver their baby in this way in the UK. This can happen because of the reasons… <span class="read-more">Read More »</span></p>
  <div class="post-meta">
    Posted in: <span class="category">Midwifery</span>
    <span class="stats">
      <span class="stat">
        <svg width="13" height="12" viewBox="0 0 13 12"><path d="M1.5 1.5h10v6.5h-6l-3 2.5v-2.5h-1z" fill="none" stroke="#f76a8c" stroke-width="1.2" stroke-linejoin="round"/></svg>
        23 comments
      </span>
      <span class="stat">
        <svg width="13" height="12" viewBox="0 0 13 12"><path d="M6.5 11 1.6 6.1a2.8 2.8 0 0 1 4.9-3.4 2.8 2.8 0 0 1 4.9 3.4z" fill="none" stroke="#f76a8c" stroke-width="1.2" stroke-linejoin="round"/></svg>
        46 likes
      </span>
    </span>
  </div>

  <aside class="sidebar"></aside>
  <h2 class="widget-heading welcome-heading">Welcome to my blog</h2>
  <div class="author-photo" role="img" aria-label="Portrait of the midwife with her two young children"></div>
  <p class="author-intro">Hello, my name is XXX and&nbsp; I'm a midwife.<br>This is my blog about catching babies and<br>coping with lifes difficult questions. Enjoy!</p>
  <ul class="social-links" aria-label="Social links"><li></li><li></li><li></li><li></li><li></li><li></li></ul>
  <h2 class="widget-heading categories-heading">Categories</h2>
  <div class="category-select">Select Category
    <svg width="14" height="8" viewBox="0 0 14 8"><path d="M1 1l6 6 6-6" fill="none" stroke="#777" stroke-width="1.3"/></svg>
  </div>
</body>
</html>
```